Bref créative
Harbor Floors & More --- Business card
Harbor Floors & More - thousands of types of tiles
Simple
Mei Dalton
4150 Marwood Ave,
Unit 3B, Concord, ON
L4K 5R8
mei.dalton@harborfloorsmore.example
www.harborfloorsmore.example
Introduction : Harbor Floors & More imports and distributes thousands of types of tiles in limestone, marble, slate, granite, porcelan, ceramic, glass and aluminum for homeowners, builders and contractors. Also providing custom-made solid wood kitchen cabinet and vanities.
the logo of Harbor Floors & More
Logo on Black
Logo on White

```html
<!DOCTYPE html>
<html lang="en">
<head>
<meta charset="utf-8">
<title>Harbor Floors &amp; More — Business Card</title>
<link rel="stylesheet" href="https://fonts.googleapis.com/css2?family=Open+Sans:wght@400;600;700&display=swap">
<style>
  :root {
    --backdrop: #e4e5e7;
    --lime: #a9c521;
    --lime-light: #c9de44;
    --lime-dark: #8aab12;
    --blue: #1ea3dc;
    --blue-dark: #1379b5;
    --ink: #3b3f44;
    --ink-soft: #6b7077;
    --card-white: #ffffff;
  }
  * { margin: 0; padding: 0; box-sizing: border-box; }
  html, body {
    width: 1200px; height: 984px; overflow: hidden;
    background: var(--backdrop);
    font-family: "Open Sans", Arial, sans-serif;
  }
  .stage {
    position: relative; width: 1200px; height: 984px;
    display: flex; flex-direction: column; align-items: center; justify-content: center; gap: 60px;
  }
  .card {
    position: relative; width: 600px; height: 343px; border-radius: 18px; overflow: hidden;
    box-shadow: 0 6px 18px rgba(0,0,0,0.12);
  }
  .card-back {
    background: linear-gradient(135deg, var(--lime-light) 0%, var(--lime) 55%, var(--lime-dark) 100%);
  }
  .card-back .web-line {
    position: absolute; left: 40px; bottom: 70px;
    color: #fff; font-size: 17px; letter-spacing: 2.5px; font-weight: 400;
  }
  .card-front { background: var(--card-white); }
  .card-front .swoosh { position: absolute; inset: 0; width: 100%; height: 100%; }
  .brand {
    position: absolute; left: 250px; top: 70px; display: flex; align-items: center; gap: 12px;
  }
  .brand-square { width: 30px; height: 30px; background: var(--blue); }
  .brand-name {
    color: var(--ink); font-size: 25px; font-weight: 600; letter-spacing: 0.5px; line-height: 1;
  }
  .address {
    position: absolute; left: 150px; top: 160px; width: 170px; text-align: right;
    font-size: 11px; line-height: 1.55; color: var(--ink-soft);
  }
  .contact { position: absolute; left: 345px; top: 150px; }
  .contact-name { color: var(--blue); font-size: 14px; font-weight: 700; margin-bottom: 8px; }
  .contact-list { list-style: none; }
  .contact-list li {
    display: flex; align-items: center; gap: 7px;
    font-size: 10.5px; line-height: 1; color: var(--ink-soft); margin-bottom: 6px;
  }
  .contact-icon { width: 13px; height: 13px; flex: none; }
</style>
</head>
<body>
<main class="stage">
  <section class="card card-back" aria-label="Business card back">
    <p class="web-line">www.harborfloorsmore.example</p>
  </section>

  <section class="card card-front" aria-label="Business card front">
    <svg class="swoosh" viewBox="0 0 600 343" preserveAspectRatio="none" aria-hidden="true">
      <path d="M0 175 C 120 215, 250 275, 420 343 L 0 343 Z" fill="var(--lime)"/>
      <path d="M0 175 C 140 205, 300 270, 420 343 L 395 343 C 280 285, 130 225, 0 200 Z" fill="#ffffff"/>
      <path d="M0 155 C 150 180, 330 250, 470 343 L 430 343 C 300 265, 150 205, 0 178 Z" fill="var(--blue)"/>
      <path d="M0 240 C 110 265, 220 300, 300 343 L 0 343 Z" fill="var(--lime-dark)" opacity="0.55"/>
    </svg>

    <div class="brand">
      <span class="brand-square" aria-hidden="true"></span>
      <span class="brand-name">HARBOR FLOORS &amp; MORE</span>
    </div>

    <address class="address" style="font-style:normal">
      4150 Marwood Ave,<br>Unit 3B, Concord, ON<br>L4K 5R8
    </address>

    <div class="contact">
      <p class="contact-name">Mei Dalton</p>
      <ul class="contact-list">
        <li>
          <svg class="contact-icon" viewBox="0 0 14 14" aria-hidden="true">
            <circle cx="7" cy="7" r="7" fill="var(--blue)"/>
            <path d="M4.6 3.8 L5.8 3.6 L6.4 5.2 L5.6 5.8 C6 6.8 7 7.8 8 8.2 L8.6 7.4 L10.2 8 L10 9.2 C7 9.6 4.2 6.8 4.6 3.8 Z" fill="#fff"/>
          </svg>
          647-555-0184
        </li>
        <li>
          <svg class="contact-icon" viewBox="0 0 14 14" aria-hidden="true">
            <circle cx="7" cy="7" r="7" fill="var(--blue)"/>
            <rect x="3.5" y="4.5" width="7" height="5" fill="none" stroke="#fff" stroke-width="1"/>
            <path d="M3.5 4.5 L7 7.3 L10.5 4.5" fill="none" stroke="#fff" stroke-width="1"/>
          </svg>
          mei.dalton@harborfloorsmore.example
        </li>
        <li>
          <svg class="contact-icon" viewBox="0 0 14 14" aria-hidden="true">
            <circle cx="7" cy="7" r="7" fill="var(--blue)"/>
            <circle cx="7" cy="7" r="3.6" fill="none" stroke="#fff" stroke-width="0.9"/>
            <path d="M3.4 7 H10.6 M7 3.4 C5.5 5 5.5 9 7 10.6 M7 3.4 C8.5 5 8.5 9 7 10.6" fill="none" stroke="#fff" stroke-width="0.8"/>
          </svg>
          www.harborfloorsmore.example
        </li>
      </ul>
    </div>
  </section>
</main>
</body>
</html>
```